brenwick carpentry business card 2.0

id like to get some extra info added to my current business card ,but i am also open to a new design as well ,id like it to be a clean professional look
i have attached the original card files, i have also attached the crestline trades logo and licensed builder logo that id like to add to all the current info on the old card
also the color green is important as seen in the company logo

Industry/Entity Type

Carpentry

Colors
9bcb3c

```html
<!DOCTYPE html>
<html lang="en">
<head>
<meta charset="utf-8">
<title>Brenwick Carpentry – Business Card</title>
<link rel="stylesheet" href="https://fonts.googleapis.com/css2?family=Montserrat:wght@600&family=Open+Sans:wght@400;700&display=swap">
<style>
  :root {
    --backdrop: #2a2a2c;
    --card: #141414;
    --green: #9bcb3c;
    --white: #ffffff;
    --muted: #d8d8d8;
    --badge-gold: #e9c94a;
    --badge-cream: #efe9cf;
  }
  * { box-sizing: border-box; margin: 0; padding: 0; }
  html, body {
    width: 1200px;
    height: 799px;
    overflow: hidden;
    background: var(--backdrop);
  }
  .stage {
    position: relative;
    width: 1200px;
    height: 799px;
    display: flex;
    align-items: center;
    justify-content: center;
    gap: 48px;
  }
  .card {
    position: relative;
    width: 520px;
    height: 297px;
    background: var(--card);
    border: 3px solid var(--green);
    border-radius: 4px;
    overflow: hidden;
  }
  .wordmark {
    display: flex;
    align-items: center;
    gap: 12px;
    font-family: "Montserrat", sans-serif;
    font-weight: 600;
    color: var(--white);
    letter-spacing: 0.04em;
    line-height: 1.05;
    text-transform: uppercase;
  }
  .wordmark-square {
    flex: none;
    background: var(--green);
  }
  .card-front .wordmark {
    position: absolute;
    left: 50%;
    top: 50%;
    transform: translate(-50%, -50%);
    font-size: 34px;
  }
  .card-front .wordmark-square { width: 30px; height: 30px; }
  .card-back .wordmark {
    position: absolute;
    left: 36px;
    top: 34px;
    font-size: 28px;
  }
  .card-back .wordmark-square { width: 24px; height: 24px; }
  .holder {
    position: absolute;
    left: 36px;
    top: 140px;
    font-family: "Open Sans", sans-serif;
  }
  .holder-name {
    font-weight: 700;
    font-size: 22px;
    color: var(--green);
    letter-spacing: 0.02em;
    text-transform: uppercase;
  }
  .holder-role {
    font-size: 12px;
    color: var(--muted);
    margin-top: 2px;
  }
  .contact-list {
    list-style: none;
    margin-top: 12px;
  }
  .contact-item {
    display: flex;
    align-items: center;
    gap: 10px;
    font-size: 12.5px;
    color: var(--muted);
    margin-bottom: 7px;
  }
  .contact-icon { width: 13px; height: 13px; flex: none; }
  .badges {
    position: absolute;
    right: 26px;
    bottom: 26px;
    display: flex;
    align-items: flex-end;
    gap: 10px;
  }
  .badge-square {
    width: 30px;
    height: 34px;
    background: var(--badge-gold);
    border: 2px solid #2b4a9b;
  }
  .badge-round {
    width: 46px;
    height: 46px;
    border-radius: 50%;
    background: var(--badge-cream);
    border: 3px solid #8fb33a;
  }
</style>
</head>
<body>
  <main class="stage">
    <section class="card card-front" aria-label="Card front">
      <div class="wordmark">
        <span class="wordmark-square"></span>
        <span>Brenwick<br>Carpentry</span>
      </div>
    </section>

    <section class="card card-back" aria-label="Card back">
      <div class="wordmark">
        <span class="wordmark-square"></span>
        <span>Brenwick<br>Carpentry</span>
      </div>

      <div class="holder">
        <p class="holder-name">Daniel Marsh</p>
        <p class="holder-role">Director</p>
        <ul class="contact-list">
          <li class="contact-item">
            <svg class="contact-icon" viewBox="0 0 16 16" aria-hidden="true"><path fill="#9bcb3c" d="M3.6 1.5l2.3 2.6-1.3 1.9c.9 2 2.5 3.6 4.5 4.5l1.9-1.3 2.6 2.3-1.4 2.5C6.8 13.6 2.4 9.2 1.1 3z"/></svg>
            <span>021 555 0148</span>
          </li>
          <li class="contact-item">
            <svg class="contact-icon" viewBox="0 0 16 16" aria-hidden="true"><rect x="1" y="3" width="14" height="10" rx="1" fill="#9bcb3c"/><path d="M1.5 3.5L8 9l6.5-5.5" fill="none" stroke="#141414" stroke-width="1.4"/></svg>
            <span>dan@brenwickcarpentry.co.nz</span>
          </li>
          <li class="contact-item">
            <svg class="contact-icon" viewBox="0 0 16 16" aria-hidden="true"><circle cx="8" cy="8" r="6.5" fill="none" stroke="#9bcb3c" stroke-width="1.5"/><ellipse cx="8" cy="8" rx="2.6" ry="6.5" fill="none" stroke="#9bcb3c" stroke-width="1.2"/><path d="M1.5 8h13" stroke="#9bcb3c" stroke-width="1.2"/></svg>
            <span>www.brenwickcarpentry.co.nz</span>
          </li>
        </ul>
      </div>

      <div class="badges">
        <span class="badge-square" role="img" aria-label="Crestline Trades membership badge"></span>
        <span class="badge-round" role="img" aria-label="Licensed builder badge"></span>
      </div>
    </section>
  </main>
</body>
</html>
```